Brightpaw Haven website design; Townsville's best active boarding kennel

I need a website for my Boarding Kennel busiess, Brightpaw Haven.
I also provide additional services such as grooming, training and doggy daycare. I want to emphasize that I am a small, boutique kennel, offering quality one on one care and attention to each dog daily.
I specialise mainly in working dog type breeds and again place emphasise on dogs remaining "active" and "stimulated" during their stay.
I want to play on the emotion of people who treat their dogs like their own children.
My current business card is in bright orange and black

Target Market(s)

Target market is anyone who owns a dog.

Industry/Entity Type

Training

Number of Pages Required

5+ page

Font styles to use
Script

Requirements
Must have
• online booking form
• Location Map; 42 Moss Vale Rd, Cape Cleveland QLD 4810
• Opening hours; 6am - 6pm
• New page tabs; grooming, training, boarding & daycare, a gallery page
• Small "ABOUT ME" SECTION: I am a registered breeder of border collies with Canine Registry Guild, qualified canine behaviourist and accomplished animal groomer.
Nice to have
• slideshow of gallery photos on the main page
• Flashing RECIEVE A FREE AQUARINSE WITH EVERY STAY

```html
<!DOCTYPE html>
<html lang="en">
<head>
<meta charset="utf-8">
<title>Brightpaw Haven – Booking</title>
<link rel="stylesheet" href="https://fonts.googleapis.com/css2?family=Fondamento&family=Lobster+Two:wght@700&display=swap">
<style>
  :root {
    --orange: #ff6600;
    --orange-soft: #f7a94e;
    --paper: #fbfbfb;
    --ink: #111111;
    --white: #ffffff;
    --charcoal: #333333;
    --photo-grass: #8a8a3a;
    --photo-coat: #c8844a;
  }
  * { box-sizing: border-box; margin: 0; padding: 0; }
  html, body { width: 1200px; height: 900px; overflow: hidden; }
  body {
    position: relative;
    background: var(--paper);
    font-family: "Fondamento", cursive;
    color: var(--ink);
  }
  .hero-photo {
    position: absolute; left: 0; top: 0; width: 1200px; height: 78px;
    background: linear-gradient(90deg, #9a9a45 0%, #b7a65a 25%, #a69a4e 45%, var(--photo-coat) 62%, #b5773f 75%, var(--photo-grass) 100%);
  }
  .booking {
    position: absolute; left: 0; top: 78px; width: 1200px; height: 536px;
    background: var(--paper);
  }
  .booking-title {
    position: absolute; left: 460px; top: 25px; width: 235px; height: 70px;
    background: var(--orange); color: var(--white);
    border-radius: 3px; box-shadow: 0 4px 8px rgba(0,0,0,.3);
    font-family: "Lobster Two", cursive; font-weight: 700; font-size: 28px;
    display: flex; align-items: center; justify-content: center;
  }
  .field {
    position: absolute; background: var(--white);
    border: 1px solid var(--orange-soft);
    font-size: 22px; padding: 16px 16px; color: var(--ink);
    white-space: nowrap;
  }
  .field-name    { left: 125px; top: 126px; width: 459px; height: 57px; }
  .field-subject { left: 610px; top: 126px; width: 459px; height: 57px; }
  .field-email   { left: 125px; top: 212px; width: 459px; height: 57px; }
  .field-phone   { left: 610px; top: 212px; width: 459px; height: 57px; }
  .field-message { left: 125px; top: 299px; width: 944px; height: 125px; padding-top: 12px; }
  .send-button {
    position: absolute; left: 126px; top: 456px; width: 165px; height: 52px;
    border: 4px solid var(--orange-soft); background: var(--white);
    font-family: "Fondamento", cursive; font-size: 22px; color: var(--ink);
    display: flex; align-items: center; justify-content: center;
  }
  .site-footer {
    position: absolute; left: 0; top: 614px; width: 1200px; height: 256px;
    background: var(--orange); color: var(--white);
  }
  .footer-heading {
    font-family: "Lobster Two", cursive; font-weight: 700; font-size: 21px;
    white-space: nowrap;
  }
  .link-column { position: absolute; top: 18px; }
  .link-column-one { left: 122px; }
  .link-column-two { left: 382px; }
  .link-list { list-style: none; margin-top: 14px; }
  .link-list li {
    display: flex; align-items: center; gap: 6px;
    font-size: 19px; height: 34.5px; white-space: nowrap;
  }
  .link-list li.indented { padding-left: 8px; }
  .paw { width: 26px; height: 22px; flex: none; }
  .testimonial {
    position: absolute; left: 632px; top: 18px; width: 470px;
  }
  .testimonial .footer-heading { text-align: center; padding-right: 18px; }
  .avatar-photo {
    display: block; width: 68px; height: 68px; margin: 6px 0 0 192px;
    border-radius: 50%; border: 3px solid var(--white);
    background: radial-gradient(circle at 50% 45%, #8a6a4a, #4a3628 70%, #cfc6bb);
  }
  .quote {
    font-size: 16px; line-height: 28px; margin-top: 2px; white-space: nowrap;
  }
  .quote-author {
    text-align: right; font-size: 16px; line-height: 28px;
    padding-right: 18px; white-space: nowrap;
  }
  .bottom-bar {
    position: absolute; left: 0; top: 870px; width: 1200px; height: 30px;
    background: var(--charcoal); color: #cfcfcf; overflow: hidden;
  }
  .copyright { position: absolute; left: 122px; top: 20px; font-size: 15px; white-space: nowrap; }
  .social { position: absolute; left: 866px; top: 22px; display: flex; gap: 18px; }
  .social span { width: 20px; height: 20px; border-radius: 50%; background: var(--orange-soft); }
</style>
</head>
<body>
  <div class="hero-photo" role="img" aria-label="Blurred photo of a happy dog lying on green grass"></div>

  <section class="booking">
    <h1 class="booking-title">Booking Now</h1>
    <div class="field field-name">Name</div>
    <div class="field field-subject">Subject</div>
    <div class="field field-email">Email</div>
    <div class="field field-phone">Phone Number</div>
    <div class="field field-message">Message</div>
    <div class="send-button">Send</div>
  </section>

  <svg width="0" height="0" style="position:absolute">
    <defs>
      <symbol id="paw" viewBox="0 0 26 22">
        <ellipse cx="15" cy="14" rx="7" ry="6"/>
        <ellipse cx="5" cy="6" rx="3" ry="3.5"/>
        <ellipse cx="4" cy="14" rx="3" ry="3.2"/>
        <ellipse cx="10" cy="3.5" rx="3" ry="3.2"/>
        <ellipse cx="6" cy="20" rx="2.6" ry="2"/>
      </symbol>
    </defs>
  </svg>

  <footer class="site-footer">
    <div class="link-column link-column-one">
      <h2 class="footer-heading">Lorem ipsum dolor</h2>
      <ul class="link-list">
        <li class="indented"><svg class="paw" fill="#ffffff"><use href="#paw"/></svg>consectetuer adipiscin</li>
        <li><svg class="paw" fill="#000000"><use href="#paw"/></svg>sed diam nonummy nibh</li>
        <li><svg class="paw" fill="#000000"><use href="#paw"/></svg>euismod tincidunt ut</li>
        <li><svg class="paw" fill="#000000"><use href="#paw"/></svg>laoreet dolore magna</li>
      </ul>
    </div>
    <div class="link-column link-column-two">
      <h2 class="footer-heading">Lorem ipsum dolor</h2>
      <ul class="link-list">
        <li><svg class="paw" fill="#000000"><use href="#paw"/></svg>consectetuer adipiscin</li>
        <li><svg class="paw" fill="#000000"><use href="#paw"/></svg>sed diam nonummy nibh</li>
        <li><svg class="paw" fill="#000000"><use href="#paw"/></svg>euismod tincidunt ut</li>
        <li><svg class="paw" fill="#000000"><use href="#paw"/></svg>laoreet dolore magna</li>
      </ul>
    </div>
    <div class="testimonial">
      <h2 class="footer-heading">Our Customer Says</h2>
      <span class="avatar-photo" role="img" aria-label="Round portrait photo of a customer's small long-haired dog"></span>
      <p class="quote">“Lorem ipsum dolor sit amet, consectetuer adipiscing elit,<br>&nbsp;sed diam nonummy nibh euismod tincidunt ut laoreet dolore<br>magna aliquam erat volutpat. Ut wisi enim ad.</p>
      <p class="quote-author">- Lorem ipsum.</p>
    </div>
  </footer>

  <div class="bottom-bar">
    <p class="copyright">Copyright 2024 Brightpaw Haven. All rights reserved. Designed with care.</p>
    <div class="social" aria-label="Social links"><span></span><span></span><span></span></div>
  </div>
</body>
</html>
```